design for a mobile ultrasound business
A Professional, clean, inviting look
Professional
Lionel K. Hargrove, BS, RCS
48207 Tarn Ave.
Suite # 317
N. Chesterfield, VA 23418
clearwavescans@brenlowmail.com
Just the Logo
Vector Logo

```html
<!DOCTYPE html>
<html lang="en">
<head>
<meta charset="utf-8">
<title>Clearwave Scan Partners — Stationery Concepts</title>
<link href="https://fonts.googleapis.com/css2?family=Montserrat:wght@400;700&family=Open+Sans:wght@400;600&display=swap" rel="stylesheet">
<style>
  :root{
    --navy:#14236e;
    --blue:#2447a6;
    --green:#5bb03a;
    --paper:#ffffff;
    --ink:#3a3f4a;
    --muted:#8a8f99;
    --bg-top:#9a9a9a;
    --bg-bottom:#c4c4c4;
  }
  *{margin:0;padding:0;box-sizing:border-box}
  html,body{width:1200px;height:314px;overflow:hidden}
  body{background:linear-gradient(180deg,var(--bg-top),var(--bg-bottom));position:relative;font-family:"Open Sans",sans-serif;color:var(--ink)}
  .item{position:absolute;background:var(--paper);box-shadow:0 3px 8px rgba(0,0,0,.35);overflow:hidden}
  .brand{display:flex;align-items:center;gap:4px}
  .brand-dot{border-radius:50%;background:var(--green);flex:none}
  .brand-name{font-family:"Montserrat",sans-serif;font-weight:700;color:var(--navy);text-transform:uppercase;line-height:1.05}
  .board-title{position:absolute;left:24px;top:50px}
  .board-title .brand-dot{width:34px;height:34px}
  .board-title .brand-name{font-size:15px;color:#fff;width:130px}
  .board-caption{position:absolute;left:62px;top:140px;font-family:"Montserrat",sans-serif;font-size:12px;color:#fff}
  .swoosh{position:absolute;inset:0;width:100%;height:100%}
  .details{position:absolute;font-size:5px;line-height:1.35;color:var(--ink);white-space:nowrap}
  .details strong{font-weight:600;color:var(--navy)}
  .card-back{background:var(--navy)}
  .card-back .brand-name{color:#fff}
  .letter .letter-brand{position:absolute;left:26px;top:12px}
  .letter .letter-brand .brand-dot{width:10px;height:10px}
  .letter .letter-brand .brand-name{font-size:5px;width:46px}
  .letter .letter-address{right:8px;top:11px;font-size:3.6px;text-align:left}
  .letter .body{position:absolute;left:26px;top:64px;right:14px;font-size:4.6px;line-height:1.6;color:var(--ink)}
  .letter .body p{margin-bottom:5px}
  .letter .sign{position:absolute;left:26px;bottom:40px;font-size:4.6px}
  .deco-circle{position:absolute;border-radius:50%;background:var(--navy);opacity:.06}
</style>
</head>
<body>

  <header class="board-title brand">
    <span class="brand-dot"></span>
    <span class="brand-name">Clearwave Scan Partners</span>
  </header>
  <p class="board-caption">Stationery Concepts</p>

  <!-- business card front -->
  <section class="item business-card" style="left:12px;top:180px;width:148px;height:60px">
    <svg class="swoosh" viewBox="0 0 148 60" preserveAspectRatio="none"><path d="M0 0H10Q4 30 10 60H0Z" fill="var(--navy)"/><path d="M10 0Q4 30 10 60" stroke="var(--green)" stroke-width="1.5" fill="none"/></svg>
    <div class="brand" style="position:absolute;left:16px;top:6px"><span class="brand-dot" style="width:10px;height:10px"></span><span class="brand-name" style="font-size:5px;width:48px">Clearwave Scan Partners</span></div>
    <div class="details" style="left:16px;top:26px"><strong>Lionel K. Hargrove, BS, RCS</strong><br>48207 Tarn Ave. Suite # 317<br>N. Chesterfield, VA 23418<br>clearwavescans@brenlowmail.com</div>
  </section>
  <!-- business card back -->
  <section class="item business-card card-back" style="left:168px;top:180px;width:144px;height:60px">
    <div class="brand" style="position:absolute;left:28px;top:20px"><span class="brand-dot" style="width:16px;height:16px"></span><span class="brand-name" style="font-size:7px;width:70px">Clearwave Scan Partners</span></div>
  </section>
  <section class="item business-card card-back" style="left:12px;top:247px;width:148px;height:55px">
    <div class="brand" style="position:absolute;left:12px;top:16px"><span class="brand-dot" style="width:16px;height:16px"></span><span class="brand-name" style="font-size:7px;width:70px">Clearwave Scan Partners</span></div>
  </section>
  <section class="item business-card" style="left:168px;top:247px;width:144px;height:55px">
    <svg class="swoosh" viewBox="0 0 144 55" preserveAspectRatio="none"><path d="M0 55Q70 40 144 48V55Z" fill="var(--blue)"/></svg>
    <div class="brand" style="position:absolute;left:24px;top:14px"><span class="brand-dot" style="width:14px;height:14px"></span><span class="brand-name" style="font-size:6.5px;width:66px">Clearwave Scan Partners</span></div>
  </section>

  <!-- letterheads -->
  <article class="item letter" style="left:336px;top:7px;width:164px;height:298px">
    <svg class="swoosh" viewBox="0 0 164 298" preserveAspectRatio="none"><path d="M0 0H18Q8 150 18 298H0Z" fill="var(--navy)"/><path d="M18 0Q8 150 18 298" stroke="var(--green)" stroke-width="2" fill="none"/></svg>
    <div class="brand letter-brand"><span class="brand-dot"></span><span class="brand-name">Clearwave Scan Partners</span></div>
    <div class="details letter-address">48207 Tarn Ave., Suite # 317<br>N. Chesterfield, VA 23418<br>clearwavescans@brenlowmail.com</div>
    <div class="deco-circle" style="left:50px;top:100px;width:80px;height:80px"></div>
    <div class="body"><p>Dear Patient,</p><p>Thank you for choosing our mobile ultrasound service. Our team brings clear imaging to your door.</p></div>
    <div class="sign">Sincerely,<br><strong>Lionel K. Hargrove, BS, RCS</strong></div>
  </article>
  <article class="item letter" style="left:511px;top:7px;width:164px;height:298px">
    <svg class="swoosh" viewBox="0 0 164 298" preserveAspectRatio="none"><path d="M0 0H18Q8 150 18 298H0Z" fill="var(--blue)"/><path d="M18 0Q8 150 18 298" stroke="var(--green)" stroke-width="2" fill="none"/></svg>
    <div class="brand letter-brand"><span class="brand-dot"></span><span class="brand-name">Clearwave Scan Partners</span></div>
    <div class="details letter-address">48207 Tarn Ave., Suite # 317<br>N. Chesterfield, VA 23418<br>clearwavescans@brenlowmail.com</div>
    <div class="deco-circle" style="left:50px;top:100px;width:80px;height:80px"></div>
    <div class="body"><p>Dear Patient,</p><p>Thank you for choosing our mobile ultrasound service. Our team brings clear imaging to your door.</p></div>
    <div class="sign">Sincerely,<br><strong>Lionel K. Hargrove, BS, RCS</strong></div>
  </article>

  <!-- small cards -->
  <section class="item business-card" style="left:696px;top:108px;width:122px;height:65px">
    <svg class="swoosh" viewBox="0 0 122 65" preserveAspectRatio="none"><path d="M0 0H9Q3 32 9 65H0Z" fill="var(--navy)"/><path d="M9 0Q3 32 9 65" stroke="var(--green)" stroke-width="1.5" fill="none"/></svg>
    <div class="brand" style="position:absolute;left:14px;top:6px"><span class="brand-dot" style="width:10px;height:10px"></span><span class="brand-name" style="font-size:5px;width:48px">Clearwave Scan Partners</span></div>
    <div class="details" style="left:14px;top:28px;font-size:4.5px"><strong>Lionel K. Hargrove, BS, RCS</strong><br>48207 Tarn Ave. Suite # 317<br>N. Chesterfield, VA 23418<br>clearwavescans@brenlowmail.com</div>
  </section>
  <section class="item business-card" style="left:830px;top:108px;width:130px;height:65px">
    <svg class="swoosh" viewBox="0 0 130 65" preserveAspectRatio="none"><path d="M130 0H120Q126 32 120 65H130Z" fill="var(--navy)"/><path d="M120 0Q126 32 120 65" stroke="var(--green)" stroke-width="1.5" fill="none"/></svg>
    <div class="brand" style="position:absolute;left:22px;top:22px"><span class="brand-dot" style="width:16px;height:16px"></span><span class="brand-name" style="font-size:6.5px;width:64px">Clearwave Scan Partners</span></div>
  </section>

  <!-- envelopes -->
  <section class="item envelope" style="left:696px;top:211px;width:264px;height:77px">
    <svg class="swoosh" viewBox="0 0 264 77" preserveAspectRatio="none"><path d="M0 0H12Q5 38 12 77H0Z" fill="var(--navy)"/><path d="M12 0Q5 38 12 77" stroke="var(--green)" stroke-width="1.5" fill="none"/></svg>
    <div class="brand" style="position:absolute;left:20px;top:8px"><span class="brand-dot" style="width:10px;height:10px"></span><span class="brand-name" style="font-size:5px;width:48px">Clearwave Scan Partners</span></div>
    <div class="details" style="left:20px;top:26px;font-size:4px">48207 Tarn Ave., Suite # 317<br>N. Chesterfield, VA 23418</div>
    <div class="deco-circle" style="left:150px;top:10px;width:56px;height:56px"></div>
  </section>
  <section class="item envelope" style="left:984px;top:84px;width:204px;height:96px">
    <svg class="swoosh" viewBox="0 0 204 96" preserveAspectRatio="none"><path d="M0 0H204V40Q102 30 0 55Z" fill="var(--green)"/><path d="M0 55Q102 30 204 40V96H0Z" fill="var(--blue)"/><path d="M0 0L102 55L204 0" stroke="rgba(255,255,255,.35)" stroke-width="1" fill="none"/></svg>
  </section>
  <section class="item envelope" style="left:984px;top:204px;width:204px;height:84px">
    <svg class="swoosh" viewBox="0 0 204 84" preserveAspectRatio="none"><path d="M0 0L102 46L204 0" stroke="#d8dbe2" stroke-width="1" fill="none"/><path d="M0 84L80 40M204 84L124 40" stroke="#e3e5ea" stroke-width="1" fill="none"/></svg>
    <div class="brand" style="position:absolute;left:92px;top:38px"><span class="brand-dot" style="width:10px;height:10px"></span></div>
  </section>

</body>
</html>
```